Maple Hollow Canine Massage Needs a Business Card Design

Maple Hollow Canine Massage is a new therapeutic canine massage company located in Nederland, Colorado. I need a business card design that include my logo and basic contact information.

Target Market(s)

Pet owners, veterinarians

Industry/Entity Type

Business

Contact Information for Business Card

Lydia Ferrow, CCMT
303.518.7269
lydia@maplehollowmassage.example
www.maplehollowmassage.example

Colors
6c459b
886aae
b8a6cd
a64599
b768aa
d3a5cc
fbed22

Requirements
Must have
• Font should be similar to font in logo.

```html
<!DOCTYPE html>
<html lang="en">
<head>
<meta charset="utf-8">
<title>Maple Hollow Canine Massage – Business Card</title>
<link rel="stylesheet" href="https://fonts.googleapis.com/css2?family=Montserrat:wght@500;600;700&family=Open+Sans:wght@400&display=swap">
<style>
  :root {
    --purple-deep: #6c459b;
    --purple-dark: #5a2d86;
    --purple-mid: #886aae;
    --lavender: #b8a6cd;
    --lavender-soft: #d9cde8;
    --gold: #e6c24a;
    --gold-soft: #f1dc8c;
    --ink-grey: #6b6b6b;
    --card-white: #ffffff;
    --backdrop: #ecebee;
  }
  html, body {
    margin: 0;
    padding: 0;
    width: 1200px;
    height: 1023px;
    overflow: hidden;
    background: var(--backdrop);
  }
  .stage {
    position: relative;
    width: 1200px;
    height: 1023px;
  }
  .business-card {
    position: absolute;
    left: 100px;
    top: 225px;
    width: 1000px;
    height: 572px;
    background: var(--card-white);
    box-shadow: 0 10px 30px rgba(60, 40, 90, 0.18);
    overflow: hidden;
  }
  .card-art {
    position: absolute;
    inset: 0;
  }
  .brand {
    position: absolute;
    left: 90px;
    top: 290px;
    display: flex;
    align-items: center;
    gap: 22px;
  }
  .brand-disc {
    width: 150px;
    height: 150px;
    border-radius: 50%;
    background: var(--lavender-soft);
  }
  .brand-name {
    font-family: "Montserrat", sans-serif;
    font-weight: 600;
    font-size: 22px;
    line-height: 1.25;
    letter-spacing: 1px;
    color: var(--purple-deep);
    text-transform: uppercase;
    margin: 0;
  }
  .identity {
    position: absolute;
    left: 360px;
    top: 108px;
  }
  .person-name {
    font-family: "Montserrat", sans-serif;
    font-weight: 700;
    font-size: 31px;
    letter-spacing: 0.5px;
    color: var(--purple-deep);
    text-transform: uppercase;
    margin: 0;
  }
  .credential {
    font-family: "Open Sans", sans-serif;
    font-size: 17px;
    color: var(--ink-grey);
    margin: 4px 0 18px;
  }
  .contact-list {
    list-style: none;
    margin: 0;
    padding: 0;
  }
  .contact-item {
    display: flex;
    align-items: center;
    gap: 12px;
    font-family: "Open Sans", sans-serif;
    font-size: 19px;
    color: var(--ink-grey);
    margin-bottom: 9px;
  }
  .contact-icon {
    width: 20px;
    height: 20px;
    flex: none;
  }
</style>
</head>
<body>
<main class="stage">
  <section class="business-card" aria-label="Business card front">
    <svg class="card-art" viewBox="0 0 1000 572" aria-hidden="true">
      <path class="wave-silver" d="M330 572 C560 520 690 380 780 230 C850 110 930 45 1000 20 L1000 572 Z" fill="#eeeeee"/>
      <path class="wave-gold" d="M350 572 C575 515 700 380 792 232 C862 118 935 55 1000 32 L1000 572 Z" fill="var(--gold)"/>
      <path class="wave-gold-gap" d="M372 572 C590 512 712 382 804 240 C874 128 945 68 1000 48 L1000 572 Z" fill="var(--card-white)"/>
      <path class="wave-purple" d="M400 572 C610 515 730 395 820 252 C885 148 950 90 1000 70 L1000 572 Z" fill="var(--purple-dark)"/>
      <path class="wave-inner-gold" d="M690 470 C800 380 860 250 1000 150 C880 235 820 360 690 470 Z" fill="var(--gold-soft)" opacity="0.9"/>
    </svg>

    <div class="brand">
      <div class="brand-disc"></div>
      <p class="brand-name">Maple Hollow<br>Canine Massage</p>
    </div>

    <div class="identity">
      <h1 class="person-name">Lydia Ferrow</h1>
      <p class="credential">CCMT</p>
      <ul class="contact-list">
        <li class="contact-item">
          <svg class="contact-icon" viewBox="0 0 20 20" aria-hidden="true">
            <rect width="20" height="20" rx="3" fill="var(--purple-deep)"/>
            <path d="M6 4 h3 l1 3 -2 1.5 a7 7 0 0 0 3.5 3.5 L13 10 l3 1 v3 a2 2 0 0 1 -2 2 A11 11 0 0 1 4 6 a2 2 0 0 1 2 -2 Z" fill="#fff"/>
          </svg>
          303.518.7269
        </li>
        <li class="contact-item">
          <svg class="contact-icon" viewBox="0 0 20 20" aria-hidden="true">
            <rect width="20" height="20" rx="3" fill="var(--purple-deep)"/>
            <rect x="4" y="6" width="12" height="9" fill="#fff"/>
            <path d="M4 6 L10 11 L16 6" fill="none" stroke="var(--purple-deep)" stroke-width="1.4"/>
          </svg>
          lydia@maplehollowmassage.example
        </li>
        <li class="contact-item">
          <svg class="contact-icon" viewBox="0 0 20 20" aria-hidden="true">
            <rect width="20" height="20" rx="3" fill="var(--purple-deep)"/>
            <circle cx="10" cy="10" r="6" fill="none" stroke="#fff" stroke-width="1.4"/>
            <path d="M4 10 H16 M10 4 C7 7 7 13 10 16 M10 4 C13 7 13 13 10 16" fill="none" stroke="#fff" stroke-width="1.2"/>
          </svg>
          www.maplehollowmassage.example
        </li>
      </ul>
    </div>
  </section>
</main>
</body>
</html>
```